Commercial Real Estate Company Needs Website Redesign

Velcaro is a commercial real estate firm that is based in San Diego, but has offices and properties across the U.S. The current website was completed almost 3 years ago and is need of a refresh. We will rework the existing Wordpress CMS system, but require a new design. We have a great programmer who can take the design into wordpress. I need a design template for each page types, There are are approximately 20 pages for each section of our site. There are 4 Sections: Corporate, Hospitality, Commercial/Residential, and Receiver/Bankruptcy. See attached creative brief for the initial pages we would like drafted.

Industry/Entity Type

Real Estate

```html
<!DOCTYPE html>
<html lang="en">
<head>
<meta charset="utf-8">
<title>Velcaro</title>
<link rel="stylesheet" href="https://fonts.googleapis.com/css2?family=Open+Sans:wght@400;600;700&family=Fjalla+One&display=swap">
<style>
:root{
  --page:#1b2d4b;
  --header:#1d3961;
  --orange:#f9a533;
  --orange-line:#e8952a;
  --white:#ffffff;
  --menu-bg:#f7f7f7;
  --menu-text:#7d7d7d;
  --menu-line:#e2e2e2;
  --body-text:#8c8c8c;
  --footer:#1a1a1a;
  --footer-text:#9a9a9a;
  --news-head:#25416a;
  --news-body:#1f3a62;
  --icon-line:#5a5a5a;
}
*{box-sizing:border-box;margin:0;padding:0}
html,body{width:1109px;height:1200px;overflow:hidden}
body{background:var(--page);font-family:"Open Sans",sans-serif;position:relative;color:var(--white)}
.abs{position:absolute}

/* header */
.site-header{left:160px;top:16px;width:791px;height:114px;background:var(--header)}
.brand{left:16px;top:38px;display:flex;align-items:center;gap:8px}
.brand-dot{width:18px;height:18px;border-radius:50%;background:var(--orange)}
.brand-name{font-size:31px;font-weight:600;letter-spacing:1px;line-height:1;color:var(--white)}
.call{left:496px;top:20px;display:flex;align-items:center;gap:9px;font-size:14.5px}
.social{top:18px;width:25px;height:25px;border:1.5px solid #aab6c8;border-radius:50%}
.main-nav{left:0;top:65px;width:791px;height:30px;font-size:12px}
.main-nav a{position:absolute;top:6px;color:var(--white);text-decoration:none;white-space:nowrap}
.main-nav .nav-cta{top:0;left:605px;width:78px;height:30px;background:var(--orange);border-radius:2px;text-align:center;line-height:30px}

/* dropdown */
.dropdown{left:450px;top:120px;width:176px;background:var(--menu-bg);z-index:5;box-shadow:0 2px 6px rgba(0,0,0,.25)}
.dropdown li{list-style:none;height:39.6px;line-height:39.6px;padding-left:15px;font-size:11px;color:var(--menu-text);border-top:1px solid var(--menu-line)}
.dropdown li.active{background:var(--orange);color:var(--white);font-weight:600;border-top:none}

/* hero */
.hero{left:160px;top:150px;width:589px;height:363px;background:linear-gradient(180deg,#8fb3d9 0%,#b9cde0 30%,#6f8a52 55%,#4d6b2c 80%,#8f8a7c 100%)}
.hero-caption{left:0;bottom:0;width:589px;height:46px;background:rgba(35,45,55,.75);font-family:"Fjalla One",sans-serif;font-size:16px;text-align:center;line-height:46px;letter-spacing:.3px}
.hero-arrow{top:15px}

/* sidebar */
.quick-links{left:770px;top:148px;width:181px;background:var(--orange)}
.quick-links li{list-style:none;height:40px;line-height:40px;padding-left:17px;font-size:13px;border-top:1px solid var(--orange-line)}
.quick-links li:first-child{border-top:none}
.newsletter-head{left:770px;top:364px;width:181px;height:43px;background:var(--news-head);padding-left:13px;line-height:43px;font-size:13px}
.newsletter-body{left:770px;top:407px;width:181px;height:107px;background:var(--news-body)}
.newsletter-body p{position:absolute;left:0;top:12px;width:181px;text-align:center;font-size:10px;line-height:17px}
.email-field{left:12px;top:62px;width:156px;height:24px;border:1px solid var(--orange);display:flex;font-size:9px}
.email-field span{flex:1;padding-left:8px;line-height:22px}
.email-field b{width:48px;background:var(--orange);text-align:center;line-height:22px;font-weight:700}

/* audience cards */
.card{top:538px;width:250px;height:300px;background:var(--white)}
.card-media{width:100%;height:127px}
.card-title{height:35px;background:var(--orange);font-family:"Fjalla One",sans-serif;font-size:19px;text-align:center;line-height:35px;font-weight:400}
.card-text{padding:21px 15px 0;font-size:10.1px;line-height:17.5px;color:var(--body-text);text-align:justify;letter-spacing:-.1px}

/* partners */
.partners{left:160px;top:862px;width:792px;height:87px;background:var(--white)}
.partner{position:absolute;background:#d4d9e2}

/* footer */
.site-footer{left:160px;top:949px;width:792px;height:191px;background:var(--footer)}
.foot-brand{left:28px;top:27px;display:flex;align-items:center;gap:6px}
.foot-brand .brand-dot{width:12px;height:12px}
.foot-brand .brand-name{font-size:19px}
.consult{left:27px;top:61px;width:232px;height:106px;border:1px solid #333}
.consult-line{left:11px;top:15px;font-size:13px;font-weight:600;white-space:nowrap}
.consult-line em{font-style:normal;font-family:"Fjalla One",sans-serif;font-size:19px;color:var(--orange);margin-left:4px;font-weight:400}
.consult-phone{left:84px;top:60px;font-family:"Fjalla One",sans-serif;font-size:21px;letter-spacing:.5px}
.consult-icon{left:15px;top:52px;width:52px;height:52px;border-radius:50%;background:#222;display:flex;align-items:center;justify-content:center}
.foot-heading{top:22px;font-family:"Fjalla One",sans-serif;font-size:19px;color:#bfbfbf;font-weight:400}
.map{left:298px;top:62px;width:216px;height:106px;background:linear-gradient(135deg,#e6dcc6,#d9d7c0 50%,#cfd8c3)}
.contact-icon{left:554px;width:30px;height:30px;border:1px solid var(--icon-line);display:flex;align-items:center;justify-content:center}
.contact-text{left:602px;font-size:10.5px;color:var(--footer-text);line-height:18px}
.contact-text.big{font-size:14px}

/* bottom bar */
.bottom-bar{left:160px;top:1163px;width:791px;font-size:9.5px;display:flex;justify-content:space-between}
.bottom-links span{margin-left:10px}
</style>
</head>
<body>

<header class="abs site-header">
  <div class="abs brand"><span class="brand-dot"></span><span class="brand-name">VELCARO</span></div>

  <div class="abs call">
    <svg width="24" height="22" viewBox="0 0 24 22" aria-hidden="true"><circle cx="13" cy="11" r="9" fill="none" stroke="#fff" stroke-width="1.6"/><path d="M3 6c-2 4 1 10 7 13l2-3-3-2-1 1c-2-1-3-3-3-5l1-1-2-3z" fill="#fff"/><text x="13" y="14" font-size="7" font-family="Open Sans" font-weight="700" fill="#fff" text-anchor="middle">24</text></svg>
    <span>Call : 858-555-0147</span>
  </div>
  <span class="abs social" style="left:686px"></span>
  <span class="abs social" style="left:718px"></span>
  <span class="abs social" style="left:750px"></span>

  <nav class="abs main-nav">
    <a style="left:301px">Who we are</a>
    <a style="left:394px">What&nbsp; We do</a>
    <a style="left:486px">What We’ve Done</a>
    <a class="nav-cta">Contact Us</a>
    <a style="left:699px">Velcaro Home</a>
  </nav>
</header>

<ul class="abs dropdown">
  <li class="active">About us</li>
  <li>Team</li>
  <li>News</li>
  <li>Corporate Culture</li>
  <li>Join our team</li>
  <li>Resources</li>
</ul>

<section class="abs hero" role="img" aria-label="Photo of a suburban house with a driveway, lawn and tall trees">
  <div class="abs hero-caption">CONTACT US TODAY. LET US PUT OUR EXPERTISE TO WORK FOR YOU.
    <svg class="abs hero-arrow" style="left:14px" width="12" height="16" viewBox="0 0 12 16" aria-hidden="true"><path d="M10 1L3 8l7 7" fill="none" stroke="#fff" stroke-width="3"/></svg>
    <svg class="abs hero-arrow" style="left:563px" width="12" height="16" viewBox="0 0 12 16" aria-hidden="true"><path d="M2 1l7 7-7 7" fill="none" stroke="#fff" stroke-width="3"/></svg>
  </div>
</section>

<ul class="abs quick-links">
  <li>Portfolio Map</li>
  <li>Buyer Registration</li>
  <li>Properties for Sale</li>
  <li>Industry Updates</li>
  <li>Velcaro Deskbook</li>
</ul>

<div class="abs newsletter-head">Subscribe to Newsletter</div>
<div class="abs newsletter-body">
  <p>Sign up to receive industry<br>updates&nbsp; and event invitations.</p>
  <div class="abs email-field"><span>Enter Email</span><b>SUBMIT</b></div>
</div>

<article class="abs card" style="left:160px">
  <div class="card-media" role="img" aria-label="Photo of a hand holding house keys in front of a home" style="background:linear-gradient(90deg,#c9a777,#3f84c7 60%,#2f6fb5)"></div>
  <h2 class="card-title">For Owners</h2>
  <p class="card-text">Velcaro is a full service commercial real estate and advisory firm that is based in San Diego, but has offices and properties across the continental U.S. as well as Puerto Rico and the U.S. Virgin Islands. The current website was completed almost 3 years</p>
</article>
<article class="abs card" style="left:430px">
  <div class="card-media" role="img" aria-label="Illustration of a small white house on grass held in open hands" style="background:linear-gradient(180deg,#f4f6f8,#dfe6ec 70%,#9ccf5a)"></div>
  <h2 class="card-title">For Buyers/Developers</h2>
  <p class="card-text">Velcaro is a full service commercial real estate and advisory firm that is based in San Diego, but has offices and properties across the continental U.S. as well as Puerto Rico and the U.S. Virgin Islands. The current website was completed almost 3 years</p>
</article>
<article class="abs card" style="left:702px">
  <div class="card-media" role="img" aria-label="Photo of a business handshake in front of a building" style="background:linear-gradient(180deg,#3b4552,#8b97a6 60%,#c8cfd6)"></div>
  <h2 class="card-title">For lenders</h2>
  <p class="card-text">Velcaro is a full service commercial real estate and advisory firm that is based in San Diego, but has offices and properties across the continental U.S. as well as Puerto Rico and the U.S. Virgin Islands. The current website was completed almost 3 years</p>
</article>

<section class="abs partners" aria-label="Partners">
  <span class="partner" style="left:38px;top:25px;width:53px;height:32px"></span>
  <span class="partner" style="left:117px;top:21px;width:46px;height:46px;border-radius:50%"></span>
  <span class="partner" style="left:203px;top:21px;width:44px;height:46px;border-radius:50%"></span>
  <span class="partner" style="left:287px;top:26px;width:26px;height:30px;border-radius:4px"></span>
  <span class="partner" style="left:374px;top:13px;width:62px;height:62px;border-radius:50%"></span>
  <span class="partner" style="left:487px;top:30px;width:62px;height:26px"></span>
  <span class="partner" style="left:573px;top:28px;width:41px;height:30px"></span>
  <span class="partner" style="left:664px;top:24px;width:95px;height:40px;border-radius:4px"></span>
</section>

<footer class="abs site-footer">
  <div class="abs foot-brand"><span class="brand-dot"></span><span class="brand-name">VELCARO</span></div>

  <div class="abs consult">
    <div class="abs consult-line">Call for a <em>FREE CONSULTATION</em></div>
    <div class="abs consult-icon">
      <svg width="30" height="28" viewBox="0 0 24 22" aria-hidden="true"><circle cx="13" cy="11" r="9" fill="none" stroke="#888" stroke-width="1.4"/><path d="M3 6c-2 4 1 10 7 13l2-3-3-2-1 1c-2-1-3-3-3-5l1-1-2-3z" fill="#888"/><text x="13" y="14" font-size="7" font-family="Open Sans" font-weight="700" fill="#ccc" text-anchor="middle">24</text></svg>
    </div>
    <div class="abs consult-phone">858-555-0147</div>
  </div>

  <h3 class="abs foot-heading" style="left:297px">Our Location</h3>
  <div class="abs map" role="img" aria-label="Map of the western United States showing the office location"></div>

  <h3 class="abs foot-heading" style="left:554px">Get in touch</h3>
  <div class="abs contact-icon" style="top:61px"><svg width="12" height="16" viewBox="0 0 12 16" aria-hidden="true"><path d="M6 15C2 9 1 7 1 5a5 5 0 0110 0c0 2-1 4-5 10z" fill="none" stroke="#888" stroke-width="1.4"/><circle cx="6" cy="5" r="1.8" fill="#888"/></svg></div>
  <div class="abs contact-text" style="top:57px">4120 Harbor View Ave. Suite 210&nbsp; |<br>San Diego, CA 92108</div>
  <div class="abs contact-icon" style="top:101px"><svg width="16" height="14" viewBox="0 0 16 14" aria-hidden="true"><path d="M1 4c0-2 2-3 7-3s7 1 7 3v1h-3V3H4v2H1z" fill="#888"/><rect x="3" y="6" width="10" height="7" rx="1" fill="#888"/></svg></div>
  <div class="abs contact-text big" style="top:104px">Phone 858-555-0147</div>
  <div class="abs contact-icon" style="top:141px"><svg width="16" height="12" viewBox="0 0 16 12" aria-hidden="true"><rect x="1" y="1" width="14" height="10" fill="none" stroke="#888" stroke-width="1.4"/><path d="M1 1l7 6 7-6" fill="none" stroke="#888" stroke-width="1.4"/></svg></div>
  <div class="abs contact-text big" style="top:144px">info@velcaro.com</div>
</footer>

<div class="abs bottom-bar">
  <span>©2014 Velcaro, All Rights Reserved.</span>
  <span class="bottom-links"><span>Home</span><span>&nbsp;|&nbsp;&nbsp; About</span><span>&nbsp;| Velcaro Email |</span><span>Contacts</span></span>
</div>

</body>
</html>
```